Business Card Design

A logo and business card design is required for a new podiatry business based on the Great Ocean Road, Victoria, Australia. The business will provide broad array of podiatry services to communities along the coast.

A distinctive design is sought that represents both professional allied health service delivery and the iconic location of the service, where the ocean meets the Otway ranges. Colours representative of the ocean blues, greens of the local forrest would be desirable.

Target Market(s)

GP's, other allied health professionals, members of the community with foot complaints

Industry/Entity Type

Health

Contact Information for Business Card

Sandstone Heath Podiatry
Declan Hurst
B.Pod B App Sci (HM)
Phone: 0455 731 068
Email: sandstoneheathpodiatry@mailvora.net

Requirements
Must have
• On the back of the card room allocated for appointment times.
Nice to have
• Would like the logo to incorporate a foot and the elements of the coast, whether it be ocean &/or the unique elements of the coast and the great ocean road.

```html
<!DOCTYPE html>
<html lang="en">
<head>
<meta charset="utf-8">
<title>Sandstone Heath Podiatry – Business Card</title>
<link href="https://fonts.googleapis.com/css2?family=Montserrat:wght@500;600;700&family=Questrial&display=swap" rel="stylesheet">
<style>
  :root {
    --backdrop: #e9eaec;
    --card: #ffffff;
    --ink: #111111;
    --ink-soft: #555555;
    --brand-blue: #4a86d0;
    --ocean-deep: #2a5a9a;
    --rule: #9a9a9a;
  }
  * { box-sizing: border-box; margin: 0; padding: 0; }
  html, body {
    width: 1200px; height: 800px; overflow: hidden;
    background: var(--backdrop);
  }
  .sheet {
    width: 1200px; height: 800px;
    display: flex; align-items: center; justify-content: center; gap: 60px;
  }
  .card {
    width: 520px; height: 318px;
    background: var(--card);
    box-shadow: 0 2px 10px rgba(0,0,0,0.12);
    position: relative;
  }

  /* Front */
  .card--front {
    display: flex; flex-direction: column; align-items: center;
    padding-top: 42px;
  }
  .brand {
    display: flex; flex-direction: column; align-items: center; gap: 16px;
  }
  .brand__mark {
    width: 92px; height: 92px;
    background: var(--ocean-deep);
  }
  .brand__name {
    font-family: "Montserrat", sans-serif;
    font-weight: 500;
    font-size: 19px;
    letter-spacing: 1.5px;
    color: var(--brand-blue);
    text-transform: uppercase;
  }
  .person { margin-top: 26px; text-align: center; }
  .person__name {
    font-family: "Montserrat", sans-serif;
    font-weight: 600;
    font-size: 33px;
    color: var(--ink);
    letter-spacing: 0.5px;
  }
  .person__credentials {
    font-family: "Questrial", sans-serif;
    font-size: 16px;
    color: var(--ink-soft);
    letter-spacing: 1px;
    margin-top: 6px;
  }

  /* Back */
  .card--back {
    padding: 34px 40px 30px;
    font-family: "Questrial", sans-serif;
    color: var(--ink);
  }
  .appointment__title {
    font-family: "Montserrat", sans-serif;
    font-weight: 700;
    font-size: 17px;
    letter-spacing: 1px;
  }
  .appointment__rows { margin-top: 22px; display: flex; flex-direction: column; gap: 22px; }
  .appointment__row { display: flex; gap: 26px; font-size: 13px; letter-spacing: 1px; }
  .slot { display: flex; align-items: flex-end; gap: 8px; flex: 1; }
  .slot__line { flex: 1; border-bottom: 1px solid var(--rule); height: 14px; }
  .contact {
    position: absolute; left: 40px; bottom: 28px;
    font-size: 13px; line-height: 1.7; letter-spacing: 0.5px;
  }
  .contact__label { font-family: "Montserrat", sans-serif; font-weight: 700; }
</style>
</head>
<body>
<main class="sheet">
  <section class="card card--front" aria-label="Card front">
    <div class="brand">
      <div class="brand__mark"></div>
      <p class="brand__name">Sandstone Heath Podiatry</p>
    </div>
    <div class="person">
      <h1 class="person__name">Declan Hurst</h1>
      <p class="person__credentials">B.Pod B App Sci (HM)</p>
    </div>
  </section>

  <section class="card card--back" aria-label="Card back">
    <h2 class="appointment__title">APPOINTMENT</h2>
    <div class="appointment__rows">
      <div class="appointment__row">
        <span class="slot">DATE <span class="slot__line"></span></span>
        <span class="slot">TIME <span class="slot__line"></span></span>
      </div>
      <div class="appointment__row">
        <span class="slot">DATE <span class="slot__line"></span></span>
        <span class="slot">TIME <span class="slot__line"></span></span>
      </div>
      <div class="appointment__row">
        <span class="slot">DATE <span class="slot__line"></span></span>
        <span class="slot">TIME <span class="slot__line"></span></span>
      </div>
    </div>
    <div class="contact">
      <p><span class="contact__label">Phone</span> 0455 731 068</p>
      <p><span class="contact__label">Email</span> sandstoneheathpodiatry@mailvora.net</p>
    </div>
  </section>
</main>
</body>
</html>
```